rose gold typography style landscape business card | upmarket tanning lounge

After years of receiving spray tans, we are two young professionals starting our own spray tanning business. Our point of difference is offering a complete tanning experience within a fun, edgy yet professional atmosphere.
Our ideal card would draw upon design elements from the typography example we have attached. We are hoping to have "velmira" in all lowercase in the typography style, with "TANNING LOUNGE" in much smaller uppercase font underneath but closely positioned below "velmira".
We have attached an example of a business card created by a designer on here - we like how the word on the front almost goes beyond the edges of the card itself.
But you have the design know how, so please let your creative juices flow!
We are thinking either rose gold text (matte rather than a chrome look) with a white background or rose gold freehand style typography with a charcoal background using landscape orientation. We have opted for a thicker style edgy typography to accommodate the metallic look font we are looking for.
We cannot wait to see what you create! Thanks in advance.
Harriet & Jocelyn
Project Deadline Extended
Reason: Firstly, we wish to thank each and every one of you who have provided a submission for our project. You guys are amazingly talented and we've loved watching all the designs come through.
We have decided to take our top four favourite designs to a poll with our friends and family and will therefore need to extend the deadline by a couple of days.
We do apologise for any inconvenience this may have caused and thank you for your patience and understanding!
Harriet & Jocelyn

```html
<!DOCTYPE html>
<html lang="en">
<head>
<meta charset="utf-8">
<title>velmira — business card</title>
<link rel="stylesheet" href="https://fonts.googleapis.com/css2?family=Jost:wght@300;400;500&display=swap">
<style>
  :root {
    --backdrop: #ebebeb;
    --card: #fbfbfa;
    --rose-gold: #d4886a;
    --ink: #2b2b2b;
    --shadow: rgba(0, 0, 0, 0.12);
  }
  * { box-sizing: border-box; margin: 0; padding: 0; }
  html, body {
    width: 1200px;
    height: 814px;
    overflow: hidden;
    background: var(--backdrop);
    font-family: "Jost", sans-serif;
  }
  .stage {
    position: relative;
    width: 1200px;
    height: 814px;
  }
  .card {
    position: absolute;
    top: 252px;
    width: 525px;
    height: 300px;
    background: var(--card);
    overflow: hidden;
    box-shadow: 0 6px 22px var(--shadow);
  }
  .card--front { left: 50px; }
  .card--back { left: 625px; }

  .brand-name {
    position: absolute;
    left: 96px;
    top: 92px;
    font-size: 176px;
    font-weight: 500;
    line-height: 1;
    letter-spacing: -2px;
    color: var(--rose-gold);
    white-space: nowrap;
  }
  .brand-tagline {
    position: absolute;
    right: 30px;
    top: 86px;
    font-size: 15px;
    font-weight: 400;
    letter-spacing: 3.5px;
    color: var(--rose-gold);
    text-transform: uppercase;
  }

  .contact {
    position: absolute;
    left: 58px;
    top: 52px;
    color: var(--ink);
  }
  .contact__name {
    font-size: 19px;
    font-weight: 400;
    letter-spacing: 5px;
    text-transform: uppercase;
  }
  .contact__rule {
    width: 44px;
    height: 1px;
    background: var(--ink);
    margin: 4px 0 3px;
  }
  .contact__role {
    font-size: 15px;
    font-weight: 300;
    letter-spacing: 3px;
  }
  .contact__lines {
    list-style: none;
    margin-top: 18px;
    font-size: 15px;
    font-weight: 300;
    letter-spacing: 3px;
    line-height: 1.35;
  }
</style>
</head>
<body>
<main class="stage">
  <section class="card card--front" aria-label="Card front">
    <span class="brand-tagline">Tanning Lounge</span>
    <span class="brand-name">velmira</span>
  </section>

  <section class="card card--back" aria-label="Card back">
    <div class="contact">
      <p class="contact__name">Harriet</p>
      <div class="contact__rule"></div>
      <p class="contact__role">founder</p>
      <ul class="contact__lines">
        <li>T: (555) 014229</li>
        <li>M: me@velmira.com</li>
        <li>W: www.velmira.com</li>
      </ul>
    </div>
  </section>
</main>
</body>
</html>
```